A ebook cover to reinvent the imagery of vegetable companion gardening

We needs a ebook design with illustrates minimal as well as clear and concise relevance to vegetable companion gardening . we will add a mock up design and other existing designs to help you gauge and create the sort of illustration fit for our aims.
Book Title: Harvest Patch Basics – Vegetable Partner Sowing
Subtitle: Partner Handbook For Raising Crops Through Simple, Natural & Lasting Plot Methods
(Perfect For Beginners)
Author: Tall Meadow
Size: 5.5 x 8.5

```html
<!DOCTYPE html>
<html lang="en">
<head>
<meta charset="utf-8">
<title>Harvest Patch Basics – Vegetable Partner Sowing</title>
<link rel="stylesheet" href="https://fonts.googleapis.com/css2?family=Hind:wght@500;600;700&family=Montserrat:wght@600&display=swap">
<style>
  :root {
    --page: #ffffff;
    --cover: #f8f7ef;
    --ink: #33262e;
    --rust: #c4633f;
    --leaf: #8a9a2d;
    --olive: #5e5a18;
    --teal: #2f7f86;
    --gold: #e7a23a;
    --plum: #4b3a48;
  }
  * { box-sizing: border-box; margin: 0; padding: 0; }
  html, body { width: 1200px; height: 1200px; overflow: hidden; background: var(--page); }
  .canvas { position: relative; width: 1200px; height: 1200px; }
  .book-cover {
    position: absolute; left: 243px; top: 48px; width: 714px; height: 1104px;
    background: var(--cover);
    box-shadow: 0 6px 30px rgba(0,0,0,0.12);
    font-family: "Hind", sans-serif;
    color: var(--ink);
  }
  .tagline {
    position: absolute; top: 36px; left: 0; width: 100%; text-align: center;
    font-family: "Montserrat", sans-serif; font-weight: 600;
    font-size: 19px; letter-spacing: 7px; color: var(--ink);
  }
  .produce-wreath {
    position: absolute; left: 10px; top: 78px; width: 694px; height: 740px;
    border-radius: 48% 52% 46% 54% / 50% 48% 52% 50%;
    background:
      radial-gradient(circle at 30% 25%, rgba(138,154,45,0.55), transparent 40%),
      radial-gradient(circle at 72% 20%, rgba(231,162,58,0.5), transparent 38%),
      radial-gradient(circle at 85% 55%, rgba(47,127,134,0.45), transparent 36%),
      radial-gradient(circle at 18% 62%, rgba(75,58,72,0.45), transparent 36%),
      radial-gradient(circle at 55% 88%, rgba(196,99,63,0.45), transparent 36%),
      radial-gradient(circle at 50% 50%, rgba(138,154,45,0.25), transparent 70%);
  }
  .title-badge {
    position: absolute; left: 137px; top: 252px; width: 436px; height: 436px;
    border-radius: 50%; background: #ffffff;
    border: 2px solid var(--ink);
    outline: 6px solid #ffffff;
    display: flex; flex-direction: column; align-items: center; justify-content: center;
    text-align: center;
  }
  .title-word { font-weight: 700; line-height: 0.95; }
  .title-word--harvest { color: var(--rust); font-size: 84px; }
  .title-word--basics { color: var(--leaf); font-size: 84px; }
  .title-divider {
    display: flex; align-items: center; gap: 14px;
    color: var(--ink); font-weight: 700; font-size: 52px; line-height: 1; margin: 8px 0 6px;
  }
  .title-divider::before, .title-divider::after {
    content: ""; width: 70px; height: 2px; background: var(--ink);
  }
  .series-title {
    position: absolute; top: 836px; left: 0; width: 100%; text-align: center;
    font-weight: 700; font-size: 27px; color: var(--olive); letter-spacing: 0.5px;
  }
  .subtitle {
    position: absolute; top: 896px; left: 90px; width: 534px; text-align: center;
    font-weight: 600; font-size: 19.5px; line-height: 28px; color: var(--ink);
    text-transform: uppercase;
  }
  .author {
    position: absolute; top: 1018px; left: 0; width: 100%; text-align: center;
    font-weight: 700; font-size: 46px; color: var(--ink); letter-spacing: 1px;
  }
</style>
</head>
<body>
<div class="canvas">
  <div class="book-cover">
    <p class="tagline">PERFECT FOR BEGINNERS</p>
    <div class="produce-wreath" role="img" aria-label="Hand-drawn wreath of colourful vegetables: carrot, broccoli, peppers, tomato, onion, asparagus, aubergine, cabbage, peas, potatoes and herbs"></div>
    <div class="title-badge">
      <span class="title-word title-word--harvest">HARVEST</span>
      <span class="title-divider">PATCH</span>
      <span class="title-word title-word--basics">BASICS</span>
    </div>
    <p class="series-title">VEGETABLE PARTNER SOWING</p>
    <p class="subtitle">Partner handbook for raising crops through simple, natural &amp; lasting plot methods</p>
    <p class="author">TALL MEADOW</p>
  </div>
</div>
</body>
</html>
```